Business card Zottelgarten

Business card is for a self-employed dog trainer with own dog school. Name and logo of the dog school are available. Color specifications as well. The design should be classy and minimalist, but also modern. An already existing idea would be: Front: Only the logo Back: Contact data

Font styles to use
Serif
Sans Serif
Other font styles liked:
• Trajan Pro

Colors
f78f20

Requirements
Must have
• Name: Margit Wendler-Rasch Title: Dipl. Dog Trainer Contain my logo Follow my font and color preferences (see files)

```html
<!DOCTYPE html>
<html lang="de">
<head>
<meta charset="utf-8">
<title>Zottelgarten – Business Card Set</title>
<link rel="stylesheet" href="https://fonts.googleapis.com/css2?family=Cinzel:wght@400;700&display=swap">
<style>
  :root {
    --orange: #f78f20;
    --card-dark: #1f1f1f;
    --white: #ffffff;
    --text-light: #e9e9e9;
    --board-light: #1b97d6;
    --board-dark: #0b5c92;
  }
  html, body {
    margin: 0;
    padding: 0;
    width: 1200px;
    height: 1000px;
    overflow: hidden;
  }
  .board {
    position: relative;
    width: 1200px;
    height: 1000px;
    background: radial-gradient(ellipse at 25% 35%, var(--board-light) 0%, #1281c0 45%, var(--board-dark) 100%);
  }
  .card {
    position: absolute;
    width: 520px;
    height: 288px;
    box-shadow: 3px 4px 8px rgba(0, 0, 0, 0.45);
    overflow: hidden;
  }
  .card svg { display: block; }
  .card--front-a { left: 61px; top: 39px; }
  .card--back-a  { left: 619px; top: 39px; }
  .card--front-b { left: 61px; top: 356px; }
  .card--back-b  { left: 619px; top: 356px; }
  .card--front-c { left: 61px; top: 673px; height: 289px; }
  .card--back-c  { left: 619px; top: 673px; height: 289px; }

  .brand-name {
    font-family: "Cinzel", serif;
    font-weight: 400;
    fill: var(--orange);
  }
  .brand-url {
    font-family: "Cinzel", serif;
    font-weight: 400;
    fill: var(--text-light);
    font-size: 10px;
    letter-spacing: 4.2px;
  }
  .person-name {
    font-family: "Cinzel", serif;
    font-weight: 700;
    fill: var(--white);
    font-size: 16px;
    letter-spacing: 0.6px;
  }
  .person-title {
    font-family: "Cinzel", serif;
    font-weight: 400;
    fill: var(--white);
    font-size: 16px;
    letter-spacing: 0.6px;
  }
  .contact {
    font-family: "Cinzel", serif;
    font-weight: 400;
    font-size: 16px;
    letter-spacing: 0.3px;
  }
  .contact--orange { fill: var(--orange); }
  .contact--white { fill: var(--white); }
  .brand-dot { fill: var(--orange); }
  .brand-ring { fill: none; stroke: var(--orange); stroke-width: 1.2; }
  .bg-dark { fill: var(--card-dark); }
  .bg-orange { fill: var(--orange); }
  .bg-white { fill: var(--white); }
</style>
</head>
<body>
<main class="board">

  <!-- Row 1 -->
  <section class="card card--front-a" aria-label="Card front">
    <svg width="520" height="288" viewBox="0 0 520 288">
      <rect class="bg-dark" width="520" height="288"/>
      <circle class="brand-ring" cx="260" cy="121" r="64"/>
      <circle class="brand-dot" cx="260" cy="121" r="60"/>
      <text class="brand-name" x="260" y="220" text-anchor="middle" font-size="31" letter-spacing="1.5">ZOTTELGARTEN</text>
      <text class="brand-url" x="260" y="231" text-anchor="middle">WWW.ZOTTELGARTEN.CH</text>
    </svg>
  </section>

  <section class="card card--back-a" aria-label="Card back">
    <svg width="520" height="288" viewBox="0 0 520 288">
      <rect class="bg-dark" width="520" height="288"/>
      <circle class="brand-ring" cx="260" cy="69" r="41"/>
      <circle class="brand-dot" cx="260" cy="69" r="38"/>
      <text class="brand-name" x="260" y="130" text-anchor="middle" font-size="20" letter-spacing="1.5">ZOTTELGARTEN</text>
      <text class="person-name" x="260" y="180" text-anchor="middle">MARGIT WENDLER-RASCH</text>
      <text class="person-title" x="260" y="200" text-anchor="middle">DIPL. DOG TRAINER</text>
      <text class="contact contact--orange" x="20" y="261">LINDENWEG 12, KIRCHBERG</text>
      <text class="contact contact--orange" x="500" y="261" text-anchor="end">TEL: (321) 555-0147</text>
    </svg>
  </section>

  <!-- Row 2 -->
  <section class="card card--front-b" aria-label="Card front">
    <svg width="520" height="288" viewBox="0 0 520 288">
      <rect class="bg-dark" width="520" height="288"/>
      <circle class="brand-ring" cx="260" cy="121" r="64"/>
      <circle class="brand-dot" cx="260" cy="121" r="60"/>
      <text class="brand-name" x="260" y="220" text-anchor="middle" font-size="31" letter-spacing="1.5">ZOTTELGARTEN</text>
      <text class="brand-url" x="260" y="231" text-anchor="middle">WWW.ZOTTELGARTEN.CH</text>
    </svg>
  </section>

  <section class="card card--back-b" aria-label="Card back">
    <svg width="520" height="288" viewBox="0 0 520 288">
      <rect class="bg-dark" width="520" height="288"/>
      <text class="person-name" x="480" y="46" text-anchor="end">MARGIT WENDLER-RASCH</text>
      <text class="person-title" x="480" y="65" text-anchor="end">DIPL. DOG TRAINER</text>
      <rect class="bg-orange" x="485" y="32" width="4" height="35"/>
      <circle class="brand-ring" cx="96" cy="136" r="55"/>
      <circle class="brand-dot" cx="96" cy="136" r="51"/>
      <text class="brand-name" x="97" y="209" text-anchor="middle" font-size="16" letter-spacing="1.2">ZOTTELGARTEN</text>
      <text class="contact contact--white" x="491" y="237" text-anchor="end">TEL: (321) 555-0147</text>
      <text class="contact contact--white" x="491" y="257" text-anchor="end">LINDENWEG 12, KIRCHBERG</text>
    </svg>
  </section>

  <!-- Row 3 -->
  <section class="card card--front-c" aria-label="Card front">
    <svg width="520" height="289" viewBox="0 0 520 289">
      <rect class="bg-orange" width="520" height="289"/>
      <ellipse class="bg-white" cx="260" cy="144" rx="258" ry="256"/>
      <ellipse class="bg-dark" cx="260" cy="144" rx="236" ry="234"/>
      <circle class="brand-ring" cx="260" cy="123" r="64"/>
      <circle class="brand-dot" cx="260" cy="123" r="60"/>
      <text class="brand-name" x="260" y="222" text-anchor="middle" font-size="31" letter-spacing="1.5">ZOTTELGARTEN</text>
      <text class="brand-url" x="260" y="233" text-anchor="middle">WWW.ZOTTELGARTEN.CH</text>
    </svg>
  </section>

  <section class="card card--back-c" aria-label="Card back">
    <svg width="520" height="289" viewBox="0 0 520 289">
      <rect class="bg-white" width="520" height="289"/>
      <ellipse class="bg-orange" cx="260" cy="144" rx="250" ry="248"/>
      <ellipse class="bg-dark" cx="260" cy="144" rx="242" ry="240"/>
      <circle class="brand-ring" cx="267" cy="61" r="40"/>
      <circle class="brand-dot" cx="267" cy="61" r="37"/>
      <text class="brand-name" x="266" y="122" text-anchor="middle" font-size="19" letter-spacing="1.5">ZOTTELGARTEN</text>
      <text class="person-name" x="266" y="173" text-anchor="middle">MARGIT WENDLER-RASCH</text>
      <text class="person-title" x="266" y="193" text-anchor="middle">DIPL. DOG TRAINER</text>
      <text class="contact contact--orange" x="266" y="228" text-anchor="middle">TEL: (321) 555-0147</text>
      <text class="contact contact--orange" x="266" y="268" text-anchor="middle">LINDENWEG 12, KIRCHBERG</text>
    </svg>
  </section>

</main>
</body>
</html>
```